Harborline Keys Realty business card design

Looking for an upscale and clean business card design and updated logo. I sell to a very high-end south Florida real estate market.
Target Market(s)
High-end real estate in south Florida real estate market
Industry/Entity Type
Real Estate Agent
Contact Information for Business Card
Harborline Keys Realty, Inc
738 West Pinecrest Ave, Suite 410/520, Fort Lauderdale, FL 33318
Carl Whitmore - Broker/Owner
954-555-0172 Direct
carlhomes@mailvista.example
Website: StayPinecrest.example
Font styles to use
Other font styles liked:
- Copperplate Gothic, Georgia, etc.
Requirements
Must have
- My photo, company name, my name and title, all info stated in Details above
Nice to have
- Luxury home design element, waterfront

```html
<!DOCTYPE html>
<html lang="en">
<head>
<meta charset="utf-8">
<title>Harborline Keys Realty – Business Card</title>
<link rel="stylesheet" href="https://fonts.googleapis.com/css2?family=Cinzel:wght@700&family=Montserrat:wght@400;500&display=swap">
<style>
  :root {
    --page-bg: #2b2b2b;
    --card-black: #161616;
    --card-charcoal: #1d1d1d;
    --gold: #f2c230;
    --gold-deep: #c99a1c;
    --white: #ffffff;
    --photo-light: #e4e2dc;
    --photo-blue: #2d4a9a;
  }
  * { margin: 0; padding: 0; box-sizing: border-box; }
  html, body { width: 1200px; height: 900px; overflow: hidden; }
  body {
    background: var(--page-bg);
    font-family: "Montserrat", sans-serif;
    color: var(--white);
    position: relative;
  }
  .card {
    position: absolute;
    left: 340px;
    width: 520px;
    height: 297px;
    overflow: hidden;
  }
  .card-back { top: 130px; }
  .card-front { top: 470px; background: var(--card-black); }

  /* back side */
  .back-pattern {
    position: absolute; inset: 0;
    background:
      radial-gradient(ellipse at 10% 30%, rgba(120,120,120,0.35), transparent 55%),
      linear-gradient(100deg, #3a3a3a 0%, #222 40%, #121212 70%, #0e0e0e 100%);
  }
  .back-brand {
    position: absolute;
    right: 34px;
    top: 186px;
    display: flex;
    align-items: center;
    gap: 8px;
    font-family: "Cinzel", serif;
    font-weight: 700;
    font-size: 12px;
    color: var(--gold);
    letter-spacing: 0.5px;
  }
  .brand-dot {
    width: 14px; height: 14px;
    border-radius: 50%;
    background: var(--gold);
  }

  /* front side */
  .front-shapes { position: absolute; inset: 0; }
  .front-brand {
    position: absolute;
    left: 36px; top: 48px;
    display: flex; align-items: center; gap: 10px;
    font-family: "Cinzel", serif;
    font-weight: 700;
    font-size: 13px;
    line-height: 1.3;
    color: var(--gold);
  }
  .front-brand .brand-dot { width: 26px; height: 26px; }
  .name-band {
    position: absolute;
    left: 0; top: 113px;
    width: 260px; height: 37px;
    background: linear-gradient(90deg, var(--gold) 0%, var(--gold-deep) 45%, rgba(201,154,28,0) 100%);
  }
  .agent-name {
    position: absolute;
    left: 33px; top: 113px;
    font-family: "Cinzel", serif;
    font-weight: 700;
    font-size: 17px;
    letter-spacing: 2px;
    line-height: 1.1;
  }
  .agent-title {
    position: absolute;
    left: 33px; top: 133px;
    font-size: 11.5px;
    line-height: 1.2;
  }
  .company-name {
    position: absolute;
    left: 33px; top: 160px;
    font-size: 10.5px;
    color: var(--gold);
  }
  .address {
    position: absolute;
    left: 33px; top: 176px;
    font-size: 10.5px;
    line-height: 1.3;
    font-style: normal;
  }
  .contact-list {
    position: absolute;
    left: 33px; top: 226px;
    list-style: none;
    font-size: 10.5px;
    line-height: 1.45;
  }
  .contact-list li { display: flex; align-items: center; gap: 8px; }
  .contact-list svg { width: 9px; height: 9px; flex: none; }
  .web-accent { color: var(--gold); }
</style>
</head>
<body>

<section class="card card-back" aria-label="Business card back">
  <div class="back-pattern" role="img" aria-label="Embossed repeating sunburst pattern fading from grey to black"></div>
  <div class="back-brand"><span class="brand-dot"></span>Harborline Keys Realty</div>
</section>

<section class="card card-front" aria-label="Business card front">
  <svg class="front-shapes" viewBox="0 0 520 297" width="520" height="297">
    <defs>
      <linearGradient id="photoTone" x1="0" y1="0" x2="1" y2="1">
        <stop offset="0" stop-color="#e9e7e1"/>
        <stop offset="0.45" stop-color="#c9c6be"/>
        <stop offset="0.75" stop-color="#3c56a0"/>
        <stop offset="1" stop-color="#24397a"/>
      </linearGradient>
    </defs>
    <polygon points="292,0 302,0 252,297 242,297" fill="var(--gold)"/>
    <polygon points="306,0 520,0 520,297 250,297" fill="url(#photoTone)" role="img" aria-label="Portrait photo of the broker in a blue blazer against a light stone wall"/>
  </svg>

  <div class="front-brand"><span class="brand-dot"></span><span>Harborline Keys<br>Realty, Inc.</span></div>

  <div class="name-band"></div>
  <h1 class="agent-name">CARL WHITMORE</h1>
  <p class="agent-title">Broker/Owner</p>

  <p class="company-name">Harborline Keys Realty, Inc</p>
  <address class="address">738 West Pinecrest Ave,<br>Suite 410/520,<br>Fort Lauderdale, FL 33318</address>

  <ul class="contact-list">
    <li>
      <svg viewBox="0 0 10 10"><path d="M2 1 L4 1 L4.6 3 L3.4 3.8 Q4.4 5.8 6.2 6.6 L7 5.4 L9 6 L9 8 Q9 9 8 9 Q1 8.5 1 2 Q1 1 2 1Z" fill="var(--gold)"/></svg>
      954-555-0172
    </li>
    <li>
      <svg viewBox="0 0 10 10"><rect x="0.5" y="2" width="9" height="6" fill="var(--gold)"/><path d="M0.5 2 L5 5.5 L9.5 2" stroke="var(--card-black)" stroke-width="0.9" fill="none"/></svg>
      carlhomes@mailvista.example
    </li>
    <li>
      <svg viewBox="0 0 10 10"><circle cx="5" cy="5" r="4.3" fill="var(--gold)"/><path d="M0.7 5 H9.3 M5 0.7 Q2.5 5 5 9.3 M5 0.7 Q7.5 5 5 9.3" stroke="var(--card-black)" stroke-width="0.7" fill="none"/></svg>
      <span>www.<span class="web-accent">StayPinecrest</span>.example</span>
    </li>
  </ul>
</section>

</body>
</html>
```